Pool Builder Website Design in arizona

Our current site is located here: tidemoor.net

We are looking to give this a modern facelift. We will be cutting your design into a wordpress theme so we can utilize the CMS plateform backend.

Look and Feel
• Clean cut and professional
• Mobile friendly
• Updated from old site
• Feel intrigued but relax (do you have trust logos? Odile looking into this)
Colors
• Warm tropical neutral colors
• Orange, brown, blues
- Please make the site modern and more sleek look that looks like a 2015 style design and NOT 1999.
- Must be coded as a wordpress theme
- must create a home page, inner page and blog page
- must allow client to BLOG using the post section in wordpress

This pool company is a pool builder/installer in Phoenix arizona.

NOTE::: Please create a home page and one internal page.

Industry/Entity Type

Builder

Coding

Coded - Design and coding required

Number of Pages Required

3 page

Font styles to use
Serif
Sans Serif

Requirements
Must have
• - Must be coded as a wordpress theme
• - must create a home page, inner page and blog page
• - must allow client to BLOG using the post section in wordpress

```html
<!DOCTYPE html>
<html lang="en">
<head>
<meta charset="utf-8">
<title>Tidemoor Pools</title>
<link href="https://fonts.googleapis.com/css2?family=Lato:ital,wght@0,400;0,700;1,400&family=Ubuntu:wght@500;700&family=Kaushan+Script&display=swap" rel="stylesheet">
<style>
:root{
  --page:#f6f6f6;
  --nav:#4a86d4;
  --navy:#1d4f9e;
  --orange:#f7941d;
  --water-1:#1e7fb0;
  --water-2:#36a9d6;
  --water-3:#0f5f8e;
  --ink:#555;
  --footer:#333;
  --footer-edge:#a9c6ec;
  --white:#fff;
}
*{box-sizing:border-box;margin:0;padding:0}
html,body{width:848px;height:1200px;overflow:hidden}
body{background:var(--page);font-family:"Lato",sans-serif;color:var(--ink);position:relative}
.abs{position:absolute}

/* header */
.nav-bar{left:0;top:46px;width:848px;height:29px;background:var(--nav);box-shadow:0 2px 3px rgba(0,0,0,.2)}
.logo-tab{left:102px;top:30px;width:170px;height:52px;background:var(--white);border-radius:0 0 30px 30px}
.brand{left:102px;top:40px;width:170px;text-align:center;font-family:"Ubuntu",sans-serif;font-weight:700;font-size:21px;color:var(--navy)}
.call{left:640px;top:8px;display:flex;align-items:center;gap:8px}
.call-icon{width:26px;height:26px;border-radius:5px;background:#7fc241;display:flex;align-items:center;justify-content:center}
.call-text{font-family:"Ubuntu",sans-serif;font-style:italic;font-size:12px;line-height:13px;color:#333;font-weight:500}
.main-nav{left:276px;top:46px;height:29px;display:flex;align-items:center}
.main-nav a{font-family:"Ubuntu",sans-serif;font-weight:700;font-size:10.5px;color:var(--white);text-decoration:none;padding:0 15px;border-left:1px solid rgba(255,255,255,.35);line-height:15px}
.main-nav a:first-child{border-left:0;color:var(--orange)}

/* hero */
.water{background:radial-gradient(ellipse at 30% 40%,var(--water-2),var(--water-1) 60%,var(--water-3))}
.hero-water{left:0;top:88px;width:848px;height:280px}
.hero-frame{left:93px;top:121px;width:662px;height:309px;background:var(--white);box-shadow:0 8px 14px rgba(0,0,0,.18)}
.hero-photo{left:99px;top:127px;width:650px;height:297px;background:linear-gradient(160deg,#6a8a4a 0%,#b9a591 30%,#c8b7a3 55%,#9d8a78 100%)}
.arrow{top:265px;color:var(--white);font-size:30px;text-shadow:0 1px 3px rgba(0,0,0,.5)}
.caption{left:220px;top:332px;width:410px;height:68px;background:rgba(60,60,60,.55)}
.caption-text{left:99px;top:336px;width:650px;text-align:center;font-size:26px;line-height:27px;color:var(--white)}
.caption-text b{color:var(--orange);font-weight:700}

/* welcome */
.welcome{left:0;top:478px;width:848px;text-align:center;font-size:23px}
.script{font-family:"Kaushan Script",cursive;color:var(--navy);font-weight:400}
.bold-orange{font-family:"Ubuntu",sans-serif;font-weight:700;color:var(--orange)}
.intro{left:134px;top:522px;width:580px;text-align:center;font-style:italic;font-size:11.5px;line-height:15px}

/* services */
.services-water{left:0;top:651px;width:848px;height:167px}
.service{top:587px;width:160px;text-align:center}
.ring{width:124px;height:124px;margin:0 auto;border-radius:50%;background:#d3d3d3;padding:6px;box-shadow:0 3px 5px rgba(0,0,0,.25)}
.thumb{width:112px;height:112px;border-radius:50%}
.service h3{font-family:"Ubuntu",sans-serif;font-weight:700;font-size:17px;color:var(--white);margin-top:14px;white-space:nowrap;text-shadow:0 1px 2px rgba(0,0,0,.3)}
.service p{font-style:italic;font-size:9.5px;line-height:13.5px;color:var(--white);margin:9px auto 0;width:148px}
.plus{display:inline-block;width:9px;height:9px;background:var(--orange);color:var(--white);font-size:9px;line-height:9px;font-style:normal;font-weight:700;vertical-align:middle}

/* lower */
.section-title{font-size:21px;top:850px;width:305px;border-bottom:1px solid #ddd;padding-bottom:8px}
.video{left:93px;top:907px;width:304px;height:166px;background:linear-gradient(135deg,#5d5240,#8a7d68 50%,#3e3a32)}
.play{left:227px;top:971px;width:37px;height:26px;background:#e02020;border-radius:7px}
.controls{left:93px;top:1044px;width:304px;height:29px;background:#1c1c1c}
.quote{left:450px;top:900px;width:305px;height:173px;background:#e6e6e6;border-radius:3px}
.label{width:60px;text-align:right;font-style:italic;font-size:10px;color:#888}
.field{left:519px;width:222px;height:21px;background:var(--white);border:1px solid #d0d0d0;border-radius:2px}
.submit{left:518px;top:1043px;width:64px;height:20px;background:#1e1e1e;border-radius:3px;color:var(--white);font-family:"Ubuntu",sans-serif;font-weight:700;font-size:12px;text-align:center;line-height:20px}

/* footer */
.footer-top{left:0;top:1115px;width:848px;height:12px;background:var(--footer-edge)}
.footer{left:0;top:1127px;width:848px;height:60px;background:var(--footer)}
.footer-bottom{left:0;top:1187px;width:848px;height:13px;background:var(--footer-edge)}
.footer-links{left:95px;top:1140px;font-size:9.5px;color:#eee}
.footer-links span{margin:0 4px;color:#aaa}
.copy{left:95px;top:1164px;font-size:9.5px;color:#eee}
.addr{left:462px;top:1134px;color:var(--white)}
.addr h4{font-weight:400;font-size:14px;display:flex;align-items:center;gap:5px}
.addr p{font-size:9.5px;line-height:12px;margin:3px 0 0 16px}
.footer-badge{left:618px;top:1120px;width:134px;height:80px;background:var(--footer-edge);border-radius:60px 60px 0 0}
.footer-brand{left:618px;top:1164px;width:134px;text-align:center;font-family:"Ubuntu",sans-serif;font-weight:700;font-size:15px;color:#3e6fae}
</style>
</head>
<body>

<header>
  <div class="abs nav-bar"></div>
  <div class="abs logo-tab"></div>
  <div class="abs brand">Tidemoor Pools</div>
  <div class="abs call">
    <div class="call-icon">
      <svg width="14" height="14" viewBox="0 0 24 24"><path fill="#fff" d="M6.6 10.8c1.4 2.8 3.8 5.1 6.6 6.6l2.2-2.2c.3-.3.7-.4 1-.2 1.1.4 2.3.6 3.6.6.6 0 1 .4 1 1V20c0 .6-.4 1-1 1C10.6 21 3 13.4 3 4c0-.6.4-1 1-1h3.5c.6 0 1 .4 1 1 0 1.3.2 2.5.6 3.6.1.3 0 .7-.2 1z"/></svg>
    </div>
    <div class="call-text">Call Us<br>555-0142-7730</div>
  </div>
  <nav class="abs main-nav">
    <a href="#">Home</a><a href="#">About Us</a><a href="#">Styles</a><a href="#">Portfolio</a><a href="#">Installation</a><a href="#">Blog</a><a href="#">Contact Us</a>
  </nav>
</header>

<section class="hero">
  <div class="abs hero-water water" role="img" aria-label="Rippling pool water background"></div>
  <div class="abs hero-frame"></div>
  <div class="abs hero-photo" role="img" aria-label="Backyard fiberglass pool with stone deck and garden"></div>
  <div class="abs arrow" style="left:112px">«</div>
  <div class="abs arrow" style="left:715px">»</div>
  <div class="abs caption"></div>
  <div class="abs caption-text">A <b>Phoenix fiberglass</b> pool is more than<br>just a relaxing piece of <b>heaven</b></div>
</section>

<section>
  <h1 class="abs welcome"><span class="script">Welcome to</span> <span class="bold-orange">Tidemoor Pools</span></h1>
  <p class="abs intro">Lorem ipsum dolor sit amet, consectetuer adipiscing elit, sed diam nonummy nibh euismod tincidut ufgkdti laoreetna all dolore magna aliquam erat volutpat. nibh euismod tincidut ufgkdti laoreetna all aliquam .</p>
</section>

<section>
  <div class="abs services-water water" role="img" aria-label="Pool water band"></div>
  <div class="abs service" style="left:93px">
    <div class="ring"><div class="thumb" role="img" aria-label="Kidney shaped fiberglass pool" style="background:radial-gradient(#4fc7ee,#2b8fb8 60%,#6b5a48)"></div></div>
    <h3>Fiberglass Pools</h3>
    <p>Lorem ipsum dolor sit amet, consectetuer adipiscing elit, sed diam nonummy . <span class="plus">+</span></p>
  </div>
  <div class="abs service" style="left:259px">
    <div class="ring"><div class="thumb" role="img" aria-label="Pool with raised spa" style="background:linear-gradient(#a08870,#3f8fd8 45%,#1f6cc0)"></div></div>
    <h3>Spools &amp; Spas</h3>
    <p>Lorem ipsum dolor sit amet, consectetuer adipiscing elit, sed diam nonummy . <span class="plus">+</span></p>
  </div>
  <div class="abs service" style="left:425px">
    <div class="ring"><div class="thumb" role="img" aria-label="Stucco outdoor fireplace" style="background:linear-gradient(#c9c3b8,#8d6e58 50%,#6e5a4a)"></div></div>
    <h3>Custom Firescapes</h3>
    <p>Lorem ipsum dolor sit amet, consectetuer adipiscing elit, sed diam nonummy . <span class="plus">+</span></p>
  </div>
  <div class="abs service" style="left:592px">
    <div class="ring"><div class="thumb" role="img" aria-label="Rock waterfall feature" style="background:linear-gradient(#b5a797,#7a6a5c 50%,#3e7fc8)"></div></div>
    <h3>Water Features</h3>
    <p>Lorem ipsum dolor sit amet, consectetuer adipiscing elit, sed diam nonummy . <span class="plus">+</span></p>
  </div>
</section>

<section>
  <h2 class="abs section-title" style="left:93px"><span class="script">Fiberglass Pool</span> <span class="bold-orange">Installation</span></h2>
  <div class="abs video" role="img" aria-label="Video of crew installing a fiberglass pool shell"></div>
  <div class="abs play"><svg width="37" height="26"><path d="M15 8l9 5-9 5z" fill="#fff"/></svg></div>
  <div class="abs controls">
    <svg width="304" height="29">
      <rect x="12" y="11" width="2" height="7" fill="#fff"/><rect x="16" y="11" width="2" height="7" fill="#fff"/>
      <rect x="27" y="13" width="170" height="3" fill="#555"/><rect x="27" y="13" width="128" height="3" fill="#e02020"/>
      <circle cx="155" cy="14.5" r="4" fill="#ddd"/>
      <rect x="220" y="10" width="9" height="9" fill="none" stroke="#888"/>
      <rect x="256" y="9" width="32" height="11" rx="5.5" fill="#333"/><circle cx="261" cy="14.5" r="6" fill="#ccc"/>
    </svg>
  </div>

  <h2 class="abs section-title" style="left:450px"><span class="script">Request</span> <span class="bold-orange">for Quote</span></h2>
  <form class="abs quote"></form>
  <div class="abs label" style="left:447px;top:917px">Name</div>
  <div class="abs field" style="top:913px"></div>
  <div class="abs label" style="left:447px;top:943px">Name</div>
  <div class="abs field" style="top:939px"></div>
  <div class="abs label" style="left:447px;top:970px">Email</div>
  <div class="abs field" style="top:966px"></div>
  <div class="abs label" style="left:447px;top:996px">Message</div>
  <div class="abs field" style="top:992px;height:44px"></div>
  <div class="abs submit">Submit</div>
</section>

<footer>
  <div class="abs footer-top"></div>
  <div class="abs footer"></div>
  <div class="abs footer-bottom"></div>
  <div class="abs footer-links">Home<span>|</span>About Us<span>|</span>Styles<span>|</span>Portfolio<span>|</span>Installation<span>|</span>Blog<span>|</span>Contact Us</div>
  <div class="abs copy">© 2015 Tidemoor Pools. All Rights Reserved.</div>
  <div class="abs addr">
    <h4><svg width="11" height="14" viewBox="0 0 24 30"><path fill="#fff" d="M12 0C5.4 0 0 5.4 0 12c0 9 12 18 12 18s12-9 12-18C24 5.4 18.6 0 12 0zm0 17a5 5 0 110-10 5 5 0 010 10z"/></svg>Tidemoor Pools</h4>
    <p>4820 W Palo Verde Rd.<br>Phoenix, AZ 85031</p>
  </div>
  <div class="abs footer-badge"></div>
  <div class="abs footer-brand">Tidemoor Pools</div>
</footer>

</body>
</html>
```